Simple elegant feminine design - Going out on my own as a Mortgage Broker.
My thoughts are the following details on the Front, middle of the card possibly? Phone and email smaller font than my name?
Marnie Veltrin
Finance Specialist
p: 0438 215 962
e: marnie@veltrinlending.com.au
Bottom of the card
residential / commercial / equipment
I would like the Font in Rose Gold maybe white or black background? or Possibly a stone grey - are you able to do a few options? I'd like them embossed
Then I had an idea as a simple logo as per the attached if you get the idea in my scribble, my initials, capital M attached to a small v that leads/follows into a circle? Thicker Font In Rose Gold, middle of the card at the back.
Very open to ideas though and what colour you think would look better with the Rose Gold.
Thanks so much for your help, I am not very creative and savvy with this stuff :-)
Industry/Entity Type
Finance
Contact Information for Business Card
Marnie Veltrin
p: 0438 215 962
Look and feel

```html
<!DOCTYPE html>
<html lang="en">
<head>
<meta charset="utf-8">
<title>Marnie Veltrin — Business Cards</title>
<link href="https://fonts.googleapis.com/css2?family=Open+Sans:wght@400;600;700&display=swap" rel="stylesheet">
<style>
  :root {
    --backdrop: #cfd4d3;
    --card-white: #f2f1ed;
    --card-lavender: #8f90ad;
    --ink: #1d1d1f;
    --ink-soft: #55555a;
    --rose-gold: #d09a74;
    --card-shadow: 0 14px 30px rgba(60, 66, 70, 0.22);
  }
  * { margin: 0; padding: 0; box-sizing: border-box; }
  html, body {
    width: 1200px;
    height: 900px;
    overflow: hidden;
    background: var(--backdrop);
    font-family: "Open Sans", sans-serif;
  }
  .canvas {
    position: relative;
    width: 1200px;
    height: 900px;
    display: flex;
    align-items: center;
    justify-content: center;
    gap: 60px;
  }
  .card {
    width: 500px;
    height: 305px;
    box-shadow: var(--card-shadow);
    position: relative;
  }
  .card--front {
    background: var(--card-white);
    display: flex;
    align-items: center;
    padding: 0 40px 0 52px;
    gap: 40px;
  }
  .brand {
    display: flex;
    flex-direction: column;
    align-items: center;
    gap: 10px;
    width: 120px;
    margin-top: -30px;
  }
  .brand__ring {
    width: 86px;
    height: 86px;
    border-radius: 50%;
    border: 2px solid var(--ink);
  }
  .brand__name {
    font-size: 12px;
    font-weight: 400;
    color: var(--ink);
    letter-spacing: 0.06em;
    white-space: nowrap;
  }
  .contact { color: var(--ink); margin-top: 10px; }
  .contact__name {
    font-size: 21px;
    font-weight: 700;
    letter-spacing: 0.04em;
    text-transform: uppercase;
    line-height: 1.1;
  }
  .contact__title {
    font-size: 14px;
    color: var(--ink-soft);
    margin-bottom: 12px;
  }
  .contact__line {
    font-size: 14px;
    line-height: 1.45;
  }
  .card--back {
    background: var(--card-lavender);
    display: flex;
    flex-direction: column;
    align-items: center;
    justify-content: center;
    gap: 14px;
  }
  .card--back .brand__ring {
    width: 110px;
    height: 110px;
    border: 2.5px solid var(--rose-gold);
  }
  .card--back .brand__name {
    color: var(--rose-gold);
    font-size: 14px;
  }
</style>
</head>
<body>
<main class="canvas">
  <section class="card card--front" aria-label="Card front">
    <div class="brand">
      <div class="brand__ring"></div>
      <span class="brand__name">Marnie Veltrin</span>
    </div>
    <div class="contact">
      <h1 class="contact__name">Marnie Veltrin</h1>
      <p class="contact__title">Finance Specialist</p>
      <p class="contact__line">0438 215 962</p>
      <p class="contact__line">marnie@veltrinlending.com.au</p>
      <p class="contact__line">www.veltrinlending.com.au</p>
    </div>
  </section>
  <section class="card card--back" aria-label="Card back">
    <div class="brand__ring"></div>
    <span class="brand__name">Marnie Veltrin</span>
  </section>
</main>
</body>
</html>
```